International Company needs a Letterhead & Envelope Design

Our Company name is Brightfold Harbor Limited.
We'd like to ask the Designers for the luxurious and sophisticated design. Our logo is very simple and neat with letter logos, so we look forward to more professional and refined designs from Designers.
We look forward to providing you with a great design.
Thanks very much in advance.

```html
<!DOCTYPE html>
<html lang="en">
<head>
<meta charset="utf-8">
<title>Brightfold Harbor Limited – Letterhead &amp; Envelope</title>
<link rel="stylesheet" href="https://fonts.googleapis.com/css2?family=PT+Sans:wght@400;700&display=swap">
<style>
  :root {
    --backdrop: #1d1d1d;
    --sheet-black: #151515;
    --band: #1e1e1e;
    --paper: #ffffff;
    --gold: #c9a33b;
    --name-grey: #6e6e6e;
    --text-light: #e6e6e6;
    --divider: #8a8a8a;
  }
  * { margin: 0; padding: 0; box-sizing: border-box; }
  html, body { width: 1200px; height: 847px; overflow: hidden; }
  body {
    position: relative;
    background: var(--backdrop);
    font-family: "PT Sans", sans-serif;
    color: var(--text-light);
  }
  .gold-frame { position: absolute; border: 1.5px solid var(--gold); }

  /* Letterhead reverse side */
  .letterhead-back {
    position: absolute; left: 74px; top: 79px; width: 448px; height: 635px;
    background: var(--sheet-black);
  }
  .letterhead-back .gold-frame { left: 6px; top: 7px; right: 6px; bottom: 8px; }

  /* Letterhead front */
  .letterhead {
    position: absolute; left: 161px; top: 140px; width: 449px; height: 633px;
    background: var(--paper);
  }
  .letterhead-header {
    position: absolute; left: 0; top: 0; width: 100%; height: 86px;
    background: var(--band);
  }
  .letterhead-header .gold-frame { left: 5px; top: 5px; right: 4px; bottom: 7px; }
  .company-name {
    position: absolute; font-weight: 700; color: var(--name-grey);
    letter-spacing: 0.5px; white-space: nowrap; line-height: 1;
  }
  .letterhead .company-name { left: 38px; top: 35px; font-size: 17px; }
  .address-block {
    position: absolute; right: 161px; top: 29px; text-align: right;
    font-size: 6.6px; line-height: 9px;
  }
  .header-divider {
    position: absolute; left: 328px; top: 24px; width: 1px; height: 35px;
    background: var(--divider);
  }
  .contact-list {
    position: absolute; left: 342px; top: 25px; list-style: none;
    font-size: 6.6px; line-height: 9px;
  }
  .contact-list li { display: flex; align-items: center; gap: 4px; }
  .contact-list svg { width: 6px; height: 6px; fill: var(--text-light); }

  /* Envelope */
  .envelope-flap {
    position: absolute; left: 682px; top: 394px; width: 442px; height: 100px;
    background: #191919; border-radius: 10px 10px 0 0;
  }
  .envelope {
    position: absolute; left: 670px; top: 475px; width: 454px; height: 218px;
    background: var(--sheet-black);
  }
  .envelope .gold-frame { left: 2px; top: 2px; right: 6px; bottom: 6px; }
  .envelope .company-name { left: 27px; top: 24px; font-size: 14px; }
  .return-address {
    position: absolute; left: 27px; top: 44px; font-size: 6.6px; line-height: 9px;
  }
</style>
</head>
<body>
  <div class="letterhead-back">
    <div class="gold-frame"></div>
  </div>

  <section class="letterhead">
    <header class="letterhead-header">
      <div class="gold-frame"></div>
      <div class="company-name">BRIGHTFOLD HARBOR</div>
      <address class="address-block" style="font-style:normal">
        2710 Larkspur Avenue<br>
        Cedar Hollow, NY 11020<br>
        www.brightfold.com
      </address>
      <div class="header-divider"></div>
      <ul class="contact-list">
        <li><svg viewBox="0 0 10 10"><path d="M1 3.5C1 2 2.5 1 5 1s4 1 4 2.5L7.5 4 7 3H3L2.5 4zM2.5 5h5L8.5 9h-7z"/></svg>555 0142 7781</li>
        <li><svg viewBox="0 0 10 10"><path d="M3 0h4a1 1 0 0 1 1 1v8a1 1 0 0 1-1 1H3a1 1 0 0 1-1-1V1a1 1 0 0 1 1-1zm0 1.5v6h4v-6z"/></svg>555 0198 3264</li>
        <li><svg viewBox="0 0 10 10"><path d="M2.5 0h5v3h-5zM0 3.5h10V8H8v2H2V8H0zm3 3.5v2h4V7z"/></svg>555 0176 9420</li>
        <li><svg viewBox="0 0 10 10"><path d="M0 2h10v6H0zm1 1v.4l4 2.6 4-2.6V3z"/></svg>ellis@brightfold.com</li>
      </ul>
    </header>
  </section>

  <div class="envelope-flap"></div>
  <section class="envelope">
    <div class="gold-frame"></div>
    <div class="company-name">BRIGHTFOLD HARBOR</div>
    <address class="return-address" style="font-style:normal">
      2710 Larkspur Avenue<br>
      Cedar Hollow, NY 11020
    </address>
  </section>
</body>
</html>
```